Core Investment Strategy's Super Pie Chart

We need a one page visual explanation of an investment strategy we call "Hollis/Varrowby". This strategy emphasizes a "core" portfolio that will seldom change and "perimeter" investments that will change. Our investment management firm caters to wealthy individuals. We want to project an image of strength and reliability. At the same time, we are willing to explore new concepts. I have uploaded a PDF of my graphically-challenged assistant's attempt at creating the one page visual.

Investment

```html
<!DOCTYPE html>
<html lang="en">
<head>
<meta charset="utf-8">
<title>Hollis / Varrowby Portfolio</title>
<link rel="stylesheet" href="https://fonts.googleapis.com/css2?family=Cinzel:wght@400;500&display=swap">
<style>
  :root {
    --page: #ffffff;
    --panel-light: #f1f1f1;
    --panel-mid: #dcdcdc;
    --ink: #2b2b2b;
    --core-blue: #29aae2;
    --core-blue-deep: #1b75bb;
    --alt-orange: #fbb040;
    --alt-orange-deep: #f7941d;
    --fund-tan: #c49a6c;
    --fund-tan-deep: #5b4a3f;
    --other-white: #ffffff;
    --other-grey: #6d6e71;
    --bond-grey: #58595b;
    --bond-grey-deep: #3a3a3c;
    --equity-green: #8dc63f;
    --equity-green-deep: #1e8a3c;
    --equity-line: #7dc242;
    --fund-brown: #754c29;
    --orange-text: #f15a24;
  }
  html, body {
    margin: 0;
    width: 1200px;
    height: 900px;
    overflow: hidden;
    background: var(--page);
  }
  .canvas { display: block; width: 1200px; height: 900px; }
  .title {
    font-family: "Cinzel", serif;
    font-size: 40px;
    fill: var(--ink);
    letter-spacing: 1px;
  }
  .label {
    font-family: "Cinzel", serif;
    font-size: 17px;
  }
  .label--core { fill: var(--core-blue); font-size: 15px; }
  .label--alt { fill: var(--orange-text); font-size: 15px; }
  .label--fund { fill: var(--fund-brown); font-size: 14px; }
  .label--other { fill: var(--bond-grey); font-size: 18px; }
  .label--bond { fill: var(--ink); font-size: 19px; }
  .label--equity { fill: var(--equity-line); font-size: 19px; }
  .connector-bond { fill: none; stroke: var(--bond-grey); stroke-width: 3; }
  .connector-equity { fill: none; stroke: var(--equity-line); stroke-width: 3; }
</style>
</head>
<body>
<svg class="canvas" viewBox="0 0 1200 900" xmlns="http://www.w3.org/2000/svg">
  <defs>
    <linearGradient id="panel-sheen" x1="0" y1="0" x2="1" y2="1">
      <stop offset="0" stop-color="#f4f4f4"/>
      <stop offset="0.5" stop-color="#e2e2e2"/>
      <stop offset="1" stop-color="#ededed"/>
    </linearGradient>
  </defs>

  <rect class="panel" x="37" y="166" width="1151" height="648" fill="url(#panel-sheen)"/>

  <text class="title" x="630" y="213" text-anchor="middle">Hollis / Varrowby Portfolio</text>

  <g class="ring">
    <!-- depth of the lower ring -->
    <path d="M885 513 A255 255 0 0 1 636.7 767.9 L636.7 749.9 A255 255 0 0 0 885 495 Z" fill="var(--fund-tan-deep)"/>
    <path d="M623.3 767.9 A255 255 0 0 1 375 513 L375 495 A255 255 0 0 0 623.3 749.9 Z" fill="var(--other-grey)"/>

    <path class="ring-core" d="M375 495 A255 255 0 0 1 623.3 240.1 L624.1 270.1 A225 225 0 0 0 405 495 Z" fill="var(--core-blue)"/>
    <path d="M405 495 A225 225 0 0 1 624.1 270.1 L624.3 280 A215 215 0 0 0 415 495 Z" fill="var(--core-blue-deep)"/>

    <path class="ring-alt" d="M636.7 240.1 A255 255 0 0 1 885 495 L855 495 A225 225 0 0 0 635.9 270.1 Z" fill="var(--alt-orange)"/>
    <path d="M635.9 270.1 A225 225 0 0 1 855 495 L845 495 A215 215 0 0 0 635.7 280 Z" fill="var(--alt-orange-deep)"/>

    <path class="ring-fund" d="M885 495 A255 255 0 0 1 636.7 749.9 L635.9 719.9 A225 225 0 0 0 855 495 Z" fill="var(--fund-tan)"/>
    <path class="ring-other" d="M623.3 749.9 A255 255 0 0 1 375 495 L405 495 A225 225 0 0 0 624.1 719.9 Z" fill="var(--other-white)"/>
  </g>

  <g class="pie-depth" transform="translate(0 16)">
    <path d="M630 325 A170 170 0 0 1 743.8 621.3 L651.4 518.8 A32 32 0 0 0 630 463 Z" fill="var(--equity-green-deep)"/>
    <path d="M743.8 621.3 A170 170 0 0 1 552.8 646.5 L615.5 523.5 A32 32 0 0 0 651.4 518.8 Z" fill="var(--equity-green-deep)"/>
    <path d="M552.8 646.5 A170 170 0 0 1 630 325 L630 463 A32 32 0 0 0 615.5 523.5 Z" fill="var(--bond-grey-deep)"/>
  </g>

  <g class="pie" stroke-width="3">
    <path class="slice-large-cap" d="M630 325 A170 170 0 0 1 743.8 621.3 L651.4 518.8 A32 32 0 0 0 630 463 Z" fill="var(--equity-green)" stroke="var(--equity-green-deep)"/>
    <path class="slice-mid-cap" d="M743.8 621.3 A170 170 0 0 1 707.2 646.5 L644.5 523.5 A32 32 0 0 0 651.4 518.8 Z" fill="var(--equity-green)" stroke="var(--equity-green-deep)"/>
    <path class="slice-small-cap" d="M707.2 646.5 A170 170 0 0 1 665.4 661.3 L636.7 526.3 A32 32 0 0 0 644.5 523.5 Z" fill="var(--equity-green)" stroke="var(--equity-green-deep)"/>
    <path class="slice-intl" d="M665.4 661.3 A170 170 0 0 1 552.8 646.5 L615.5 523.5 A32 32 0 0 0 636.7 526.3 Z" fill="var(--equity-green)" stroke="var(--equity-green-deep)"/>
    <path class="slice-intermediate-bonds" d="M552.8 646.5 A170 170 0 0 1 511.9 372.8 L607.8 472 A32 32 0 0 0 615.5 523.5 Z" fill="var(--bond-grey)" stroke="#222"/>
    <path class="slice-short-bonds" d="M511.9 372.8 A170 170 0 0 1 630 325 L630 463 A32 32 0 0 0 607.8 472 Z" fill="var(--bond-grey)" stroke="#222"/>
    <circle cx="630" cy="495" r="32" fill="#ffffff" stroke="none"/>
  </g>

  <g class="bond-connectors">
    <polyline class="connector-bond" points="525,360 432,360 432,503 355,503"/>
    <polyline class="connector-bond" points="470,532 355,532"/>
    <path d="M332 503 L346 494 L360 494 L350 503 L360 512 L346 512 Z" fill="var(--bond-grey)"/>
    <path d="M332 532 L346 523 L360 523 L350 532 L360 541 L346 541 Z" fill="var(--bond-grey)"/>
  </g>
  <text class="label label--bond" x="312" y="509" text-anchor="end">Short Term Bonds</text>
  <text class="label label--bond" x="322" y="538" text-anchor="end">Intermediate Bonds</text>

  <g class="equity-connectors">
    <polyline class="connector-equity" points="785,480 905,480"/>
    <polyline class="connector-equity" points="735,615 797,615 797,512 905,512"/>
    <polyline class="connector-equity" points="690,645 830,645 830,545 905,545"/>
    <polyline class="connector-equity" points="605,680 605,705 855,705 855,580 905,580"/>
    <path d="M902 471 L918 471 L930 480 L918 489 L902 489 L910 480 Z" fill="var(--equity-line)"/>
    <path d="M902 503 L918 503 L930 512 L918 521 L902 521 L910 512 Z" fill="var(--equity-line)"/>
    <path d="M902 536 L918 536 L930 545 L918 554 L902 554 L910 545 Z" fill="var(--equity-line)"/>
    <path d="M902 571 L918 571 L930 580 L918 589 L902 589 L910 580 Z" fill="var(--equity-line)"/>
  </g>
  <text class="label label--equity" x="938" y="487">Lg. Cap Equities</text>
  <text class="label label--equity" x="938" y="519">Mid Cap Equities</text>
  <text class="label label--equity" x="938" y="552">Sm. Cap Equities</text>
  <text class="label label--equity" x="938" y="589">Int'l/dev. Cap Equities</text>

  <text class="label label--core" x="292" y="290">Attractive Core</text>
  <text class="label label--core" x="292" y="313">Assets,</text>
  <text class="label label--alt" x="830" y="294">Alternative Assets</text>
  <text class="label label--fund" x="866" y="681">Actively Managed</text>
  <text class="label label--fund" x="866" y="701">Mutual Funds</text>
  <text class="label label--other" x="340" y="702">Others</text>
</svg>
</body>
</html>
```